Copper Lattice of Brave Movers

Hi - I would like your help transforming my (terrible) drawing into a graphic that pops -using hex colors I'll give you - so that I can put it into stationary and on t-shirts or tote bags. My company, the Tundrel Institute, trains social change leaders (from the sectors in the periodic table) on how to lead large-scale change. I have this vision - the "periodic table" but these are the sectors that my clients work in. If you are having trouble reading my writing, I apologize. Our hex colors are: #114769, #76984C, #80B5CF (Seagull), #8F2C63 and Rangoon Black #191919. You don't need to use all of them, but it'd be good to be consistent with our overall branding. If you can't read my writing, I will send correct spelling. The "Tundrel" with the flowers on the bottom is for a separate design bid.

Target Market(s)

nonprofit, social entrepreneurs, philanthropy, leaders

Requirements
Must have
• clean, readable font. alignment to look like periodic table of elements. heart icon for love, cat face for cats.

```html
<!DOCTYPE html>
<html lang="en">
<head>
<meta charset="utf-8">
<title>Copper Lattice of Brave Movers</title>
<link rel="stylesheet" href="https://fonts.googleapis.com/css2?family=Inter:wght@700;800&display=swap">
<style>
  :root {
    --ink: #191919;
    --paper: #f1f1f1;
    --green-face: #8db764;
    --green-edge: #76984c;
    --blue-face: #9ccbd8;
    --blue-edge: #78b1c8;
    --plum-face: #7a2358;
    --plum-edge: #8f2c63;
    --navy-face: #1f3a5c;
    --navy-edge: #2b4a7e;
    --white: #ffffff;
  }
  * { box-sizing: border-box; margin: 0; padding: 0; }
  html, body { width: 1200px; height: 889px; overflow: hidden; }
  body {
    background: linear-gradient(180deg, #f6f6f6 0%, #e6e6e6 100%);
    font-family: "Inter", Arial, sans-serif;
    position: relative;
  }
  .table { position: absolute; left: 0; top: 0; width: 1200px; height: 889px; }
  .tile {
    position: absolute;
    width: 126px; height: 126px;
    border: 9px solid var(--ink);
    border-radius: 18px;
    box-shadow: 5px 7px 0 var(--ink);
    overflow: hidden;
  }
  .tile::after {
    content: ""; position: absolute; inset: 0;
    box-shadow: inset -14px -12px 0 rgba(0,0,0,0.12);
    pointer-events: none;
  }
  .tile--green { background: var(--green-face); color: var(--ink); }
  .tile--blue  { background: var(--blue-face);  color: var(--ink); }
  .tile--plum  { background: var(--plum-face);  color: var(--white); }
  .tile--navy  { background: var(--navy-face);  color: var(--white); width: 154px; }
  .tile--green::after { box-shadow: inset -14px -12px 0 var(--green-edge); }
  .tile--blue::after  { box-shadow: inset -14px -12px 0 var(--blue-edge); }
  .tile--plum::after  { box-shadow: inset -14px -12px 0 var(--plum-edge); }
  .tile--navy::after  { box-shadow: inset -14px -12px 0 var(--navy-edge); }
  .tile__name {
    position: absolute; top: 5px; right: 4px; left: 4px;
    font-size: 17px; font-weight: 700; line-height: 17px;
    text-align: right; z-index: 1;
  }
  .tile__name--left { text-align: left; }
  .tile__name--center { text-align: center; }
  .tile__symbol {
    position: absolute; left: 6px; bottom: 6px;
    font-size: 58px; font-weight: 700; line-height: 58px;
    letter-spacing: -1px; z-index: 1;
  }
  .tile__icon { position: absolute; left: 8px; bottom: 14px; z-index: 1; }
  .cat-face {
    position: absolute; left: 6px; bottom: 12px; width: 70px; height: 52px;
    background: #e9ecec; border-radius: 40% 40% 48% 48%; z-index: 1;
  }
</style>
</head>
<body>
<main class="table" aria-label="Copper Lattice of Brave Movers">
  <!-- row 0 -->
  <div class="tile tile--green" style="left:210px;top:88px"><p class="tile__name">Anti-<br>violaci</p><p class="tile__symbol">Av</p></div>
  <div class="tile tile--plum" style="left:860px;top:88px"><p class="tile__name">Belonging</p><p class="tile__symbol">B</p></div>

  <!-- row 1 -->
  <div class="tile tile--green" style="left:210px;top:218px"><p class="tile__name">Earth<br>Childha</p><p class="tile__symbol">Ec</p></div>
  <div class="tile tile--blue" style="left:340px;top:218px"><p class="tile__name">Climate<br>Chanja</p><p class="tile__symbol">Cc</p></div>
  <div class="tile tile--blue" style="left:470px;top:218px"><p class="tile__name">Environm<br>Justia</p><p class="tile__symbol">Ej</p></div>
  <div class="tile tile--blue" style="left:600px;top:218px"><p class="tile__name">Human<br>Simta</p><p class="tile__symbol">Hs</p></div>
  <div class="tile tile--blue" style="left:730px;top:218px"><p class="tile__name">Halth<br>Las</p><p class="tile__symbol">Hl</p></div>
  <div class="tile tile--plum" style="left:860px;top:218px"><p class="tile__name">Honsing</p><p class="tile__symbol">H</p></div>

  <!-- row 2 -->
  <div class="tile tile--green" style="left:210px;top:348px"><p class="tile__name tile__name--center">Education</p><p class="tile__symbol">Ed</p></div>
  <div class="tile tile--blue" style="left:340px;top:348px"><p class="tile__name">Attn<br>Suncol</p><p class="tile__symbol">As</p></div>
  <div class="tile tile--blue" style="left:470px;top:348px"><p class="tile__name">Social<br>Justia</p><p class="tile__symbol">Sj</p></div>
  <div class="tile tile--blue" style="left:600px;top:348px"><p class="tile__name">Civil<br>Risht</p><p class="tile__symbol">Cr</p></div>
  <div class="tile tile--blue" style="left:730px;top:348px"><p class="tile__name">Health<br>Equita</p><p class="tile__symbol">He</p></div>
  <div class="tile tile--plum" style="left:860px;top:348px"><p class="tile__name">Jobs</p><p class="tile__symbol">J</p></div>

  <!-- row 3 -->
  <div class="tile tile--green" style="left:210px;top:478px"><p class="tile__name">Animal<br>Weifare</p><p class="tile__symbol">Aw</p></div>
  <div class="tile tile--blue" style="left:340px;top:478px"><p class="tile__name">Cat</p><div class="cat-face" role="img" aria-label="Cat face icon"></div></div>
  <div class="tile tile--blue" style="left:470px;top:478px"><p class="tile__name">Racial<br>Justia</p><p class="tile__symbol">Rj</p></div>
  <div class="tile tile--blue" style="left:600px;top:478px"><p class="tile__name">Inmijn<br>Risht</p><p class="tile__symbol">Av</p></div>
  <div class="tile tile--blue" style="left:730px;top:478px"><p class="tile__name tile__name--left">Behavian<br>Halth</p><p class="tile__symbol">Bh</p></div>
  <div class="tile tile--plum" style="left:860px;top:478px"><p class="tile__name tile__name--left">Inter-<br>generation</p><p class="tile__symbol">Ig</p></div>

  <!-- values row -->
  <div class="tile tile--navy" style="left:210px;top:661px"><p class="tile__name">Love</p>
    <svg class="tile__icon" width="54" height="50" viewBox="0 0 54 50" role="img" aria-label="Heart">
      <path d="M27 48 C18 38 2 30 2 15 C2 6 9 1 16 1 C21 1 25 4 27 8 C29 4 33 1 38 1 C45 1 52 6 52 15 C52 30 36 38 27 48 Z" fill="#ffffff"/>
    </svg>
  </div>
  <div class="tile tile--navy" style="left:367px;top:661px"><p class="tile__name">Anthentia</p><p class="tile__symbol">A</p></div>
  <div class="tile tile--navy" style="left:524px;top:661px"><p class="tile__name">Hhmlita</p><p class="tile__symbol">H</p></div>
  <div class="tile tile--navy" style="left:681px;top:661px"><p class="tile__name">Andacith</p><p class="tile__symbol">An</p></div>
  <div class="tile tile--navy" style="left:838px;top:661px"><p class="tile__name">Justice</p><p class="tile__symbol">J</p></div>
</main>
</body>
</html>
```